The next stage in our 106 year history in Specialised Stationery

We need a business card design(which is also adaptable for our general stationery) to suit the changing face of our business. Brevik, an Australian company has been the leader in its category since 1907. We design and print various books required by small business to comply with government legislation in regards to keeping records. Accountancy, Payroll, Vehicle usage recording, Firearms registration etc. The Brevik logo a blue diamond is one of the best known in our industry. As manual recording has declined in the last few years we have diversified into other areas: Safety Apparel, Personal Protective Equipment (PPE) and web based software for bookkeeping and Customer Relationship management(CRM). Separate logos have been adopted for each of these being: Brevik Systems, Brevik Safety, Brevik Apparel and Brevik Software each with same diamond but different colour background. This has made it easy to identify the different sectors but difficult to bring together for a Corporate identity in Business cards etc. We are looking to bring all logos together (not one logo) but still allow the logo to depict the diversity of our offering, while still being able to have a category specific logo for each of the divisions. All products go through the same distribution channel, Office Products. The final design should depict an old established company well, known and trusted but leaping forward and still retaining same values they have come to trust.

Target Market(s)

Micro to small business companies generally who employ 20 or less people.

Industry/Entity Type

Small Business

Requirements
Must have
• The diamonds are well recognised and the new design should retain the integrity of them.

```html
<!DOCTYPE html>
<html lang="en">
<head>
<meta charset="utf-8">
<title>Brevik Business Card</title>
<link href="https://fonts.googleapis.com/css2?family=Source+Sans+3:wght@400;600;700&display=swap" rel="stylesheet">
<style>
  :root {
    --bg: #e9e9e7;
    --card: #ffffff;
    --ink: #3a3a3a;
    --brand-blue: #1f63b0;
    --panel-blue: #1565b8;
    --panel-edge: #c9c9c9;
    --systems: #1f63b0;
    --software: #c8202f;
    --apparel: #3aa935;
    --safety: #e2582b;
    --white: #ffffff;
  }
  * { margin: 0; padding: 0; box-sizing: border-box; }
  html, body { width: 1200px; height: 676px; overflow: hidden; }
  body {
    background: var(--bg);
    font-family: "Source Sans 3", "Myriad Pro", Arial, sans-serif;
    color: var(--ink);
  }
  .card {
    position: absolute;
    left: 150px; top: 63px;
    width: 900px; height: 550px;
    background: var(--card);
    box-shadow: 0 6px 24px rgba(0,0,0,0.18);
    overflow: hidden;
  }
  .card-panel { position: absolute; inset: 0; }

  .brand {
    position: absolute; left: 262px; top: 46px;
    display: flex; align-items: center; gap: 12px;
    color: var(--brand-blue); font-weight: 700; font-size: 46px;
    letter-spacing: 1px; text-transform: uppercase;
  }
  .brand-square { width: 22px; height: 22px; background: var(--brand-blue); }

  .contact {
    position: absolute; left: 72px; top: 238px;
    font-size: 18px; line-height: 25px;
  }
  .contact-company { font-style: italic; }
  .contact-line { display: flex; align-items: center; gap: 8px; }
  .contact-line svg { width: 13px; height: 13px; flex: none; fill: var(--brand-blue); }

  .division {
    position: absolute;
    display: flex; align-items: center; gap: 7px;
    font-weight: 700; font-size: 15px; text-transform: uppercase; letter-spacing: .5px;
  }
  .division-square { width: 12px; height: 12px; }
  .division--systems { left: 556px; top: 112px; color: var(--systems); }
  .division--systems .division-square { background: var(--systems); }
  .division--software { left: 718px; top: 100px; color: var(--software); }
  .division--software .division-square { background: var(--software); }
  .division--apparel { left: 420px; top: 360px; color: var(--apparel); }
  .division--apparel .division-square { background: var(--apparel); }
  .division--safety { left: 548px; top: 470px; color: var(--safety); }
  .division--safety .division-square { background: var(--safety); }

  .person {
    position: absolute; left: 612px; top: 272px;
    color: var(--white);
  }
  .person-name { font-size: 34px; font-weight: 400; line-height: 38px; }
  .person-title { font-size: 24px; font-weight: 400; }
</style>
</head>
<body>
  <div class="card">
    <svg class="card-panel" width="900" height="550" viewBox="0 0 900 550" aria-hidden="true">
      <polygon points="440,258 470,250 860,550 826,550" fill="var(--panel-edge)"/>
      <polygon points="470,250 900,150 900,550 860,550" fill="var(--panel-blue)"/>
    </svg>

    <div class="brand"><span class="brand-square"></span>Brevik</div>

    <div class="division division--systems"><span class="division-square"></span>Brevik Systems</div>
    <div class="division division--software"><span class="division-square"></span>Brevik Software</div>
    <div class="division division--apparel"><span class="division-square"></span>Brevik Apparel</div>
    <div class="division division--safety"><span class="division-square"></span>Brevik Safety</div>

    <div class="contact">
      <p class="contact-company">Brevik Pty Limited</p>
      <p>Unit 4, 212 Harbour Road,</p>
      <p>Kelso, NSW 2795</p>
      <p class="contact-line"><svg viewBox="0 0 16 16"><path d="M4 1l3 3-2 2c1 2 3 4 5 5l2-2 3 3-2 3C7 14 2 9 1 3z"/></svg>61 2 5550 1842</p>
      <p class="contact-line"><svg viewBox="0 0 16 16"><rect x="4" y="0" width="8" height="16" rx="2"/></svg>000.0000.000</p>
      <p class="contact-line"><svg viewBox="0 0 16 16"><rect x="1" y="6" width="14" height="9" rx="1"/><rect x="4" y="1" width="8" height="5"/></svg>61 2 5550 1843</p>
      <p class="contact-line"><svg viewBox="0 0 16 16"><rect x="0" y="3" width="16" height="10" rx="1"/></svg>info@brevik.com.au</p>
      <p class="contact-line"><svg viewBox="0 0 16 16"><circle cx="8" cy="8" r="7"/></svg>www.brevik.com.au</p>
    </div>

    <div class="person">
      <p class="person-name">Alex Marlowe</p>
      <p class="person-title">Managing Director</p>
    </div>
  </div>
</body>
</html>
```